RM dental business card. A family dental practice.

Logo plus the following details.

RM Dental
Dr. Gareth Moulton D.D.S
Family. Implant.Cosmetic

84 Birchfall Crescent, Unit 12-13
Markham, ON L6P2K8

Tel: 905-555-0183
Fx:905-555-0147
rmdentalcare.example

On the double side:

Next app: ______________________

Please notify us at least 48hours in advance to avoid cancellation fees.

Reason: I didn't get time to view the design. The deadline is extended Mar22nd. Thank you.

Target Market(s)

Family Dental Services

Industry/Entity Type

Dental

Contact Information for Business Card

Put logo prominently and all the info along with it.

Font styles to use
Other font styles liked:
• See Logo Font

Colors
0255a3
3277b5
85acd3
00a990
33b8a4

Requirements
Must have
• Logo and the info stated above.
• See the logo color scheme.
• Or a grayscale (Black, white gray) combination
Nice to have
• A modern unique layout
Should not have
• too simple a design

```html
<!DOCTYPE html>
<html lang="en">
<head>
<meta charset="utf-8">
<title>RM Dental – Business Card</title>
<link rel="stylesheet" href="https://fonts.googleapis.com/css2?family=Arimo:wght@400;700&family=Open+Sans:wght@400;600&display=swap">
<style>
  :root {
    --stage: #1c1c1e;
    --card-light: #ffffff;
    --card-dark: #1b1b1b;
    --ink: #3a3a3a;
    --ink-soft: #555555;
    --teal: #15b3a8;
    --silver: #cfd2d6;
    --muted: #a9abae;
    --divider: #4a4a4a;
    --watermark: rgba(120, 120, 150, 0.12);
  }
  * { box-sizing: border-box; margin: 0; padding: 0; }
  html, body { width: 1200px; height: 1000px; overflow: hidden; }
  body {
    background: var(--stage);
    position: relative;
    font-family: "Open Sans", Arial, sans-serif;
  }
  .card {
    position: absolute;
    left: 320px;
    width: 560px;
    height: 320px;
    border-radius: 22px;
    overflow: hidden;
  }

  /* Appointment side */
  .card--appointment { top: 130px; background: var(--card-light); font-family: "Arimo", Arial, sans-serif; color: var(--ink); }
  .appointment__mark {
    position: absolute; left: 50%; top: 50%;
    transform: translate(-50%, -50%);
    width: 230px; height: 230px; border-radius: 50%;
    border: 10px solid var(--watermark);
    display: flex; align-items: center; justify-content: center;
    font-family: "Open Sans", Arial, sans-serif; font-weight: 600;
    font-size: 34px; color: var(--watermark);
  }
  .appointment__body { position: relative; padding: 42px 44px 0; }
  .appointment__title { display: flex; align-items: flex-end; gap: 8px; }
  .appointment__title h2 { font-size: 23px; font-weight: 700; white-space: nowrap; }
  .fill { flex: 1; border-bottom: 2px dotted #555; height: 1px; margin-bottom: 6px; }
  .field { display: flex; align-items: flex-end; gap: 6px; font-size: 15px; margin-top: 26px; }
  .field span { white-space: nowrap; }
  .appointment__note {
    position: absolute; left: 44px; right: 30px; bottom: 36px;
    color: var(--teal); font-size: 14.5px;
  }

  /* Contact side */
  .card--contact { top: 520px; background: var(--card-dark); color: var(--silver); }
  .brand {
    position: absolute; left: 40px; top: 50%; transform: translateY(-50%);
    width: 190px; display: flex; flex-direction: column; align-items: center; gap: 12px;
  }
  .brand__dot { width: 18px; height: 18px; border-radius: 50%; background: var(--silver); }
  .brand__name { font-size: 24px; font-weight: 600; color: var(--silver); }
  .contact__divider {
    position: absolute; left: 262px; top: 70px; bottom: 70px; width: 1px; background: var(--divider);
  }
  .contact__info { position: absolute; left: 290px; top: 74px; right: 20px; }
  .contact__name { font-size: 17px; font-weight: 400; letter-spacing: 0.3px; color: #f2f2f2; text-transform: uppercase; }
  .contact__tagline { font-size: 14px; color: var(--teal); margin-bottom: 12px; }
  .contact__address { font-size: 12.5px; color: var(--muted); line-height: 1.35; margin-bottom: 8px; }
  .contact__list { list-style: none; font-size: 13px; color: var(--muted); }
  .contact__list li { display: flex; align-items: center; gap: 10px; line-height: 1.55; }
  .contact__list svg { width: 12px; height: 12px; fill: var(--teal); flex: none; }
</style>
</head>
<body>

<section class="card card--appointment" aria-label="Appointment side">
  <div class="appointment__mark" aria-hidden="true">RM Dental</div>
  <div class="appointment__body">
    <div class="appointment__title"><h2>Next Appointment:</h2><div class="fill"></div></div>
    <div class="field"><div class="fill" style="margin-left:0"></div><span>AM/PM</span></div>
    <div class="field"><span>FOR</span><div class="fill"></div></div>
    <div class="field">
      <span>DATE</span><div class="fill"></div><span>/</span><div class="fill"></div><span>AT</span><div class="fill" style="flex:1.4"></div>
    </div>
  </div>
  <p class="appointment__note">Please notify us at least 48hours in advance to avoid cancellation fees.</p>
</section>

<section class="card card--contact" aria-label="Contact side">
  <div class="brand">
    <span class="brand__dot" aria-hidden="true"></span>
    <span class="brand__name">RM Dental</span>
  </div>
  <div class="contact__divider"></div>
  <div class="contact__info">
    <h1 class="contact__name">Dr. Gareth Moulton D.D.S</h1>
    <p class="contact__tagline">Family. Implant.Cosmetic</p>
    <p class="contact__address">84 Birchfall Crescent, Unit 12-13<br>Markham, ON L6P2K8</p>
    <ul class="contact__list">
      <li>
        <svg viewBox="0 0 24 24" aria-label="Phone"><path d="M6.6 10.8a15 15 0 0 0 6.6 6.6l2.2-2.2a1 1 0 0 1 1-.25 11.4 11.4 0 0 0 3.6.57 1 1 0 0 1 1 1V20a1 1 0 0 1-1 1A17 17 0 0 1 3 4a1 1 0 0 1 1-1h3.5a1 1 0 0 1 1 1c0 1.25.2 2.45.57 3.57a1 1 0 0 1-.25 1z"/></svg>
        905-555-0183
      </li>
      <li>
        <svg viewBox="0 0 24 24" aria-label="Fax"><path d="M6 2h10l2 2v5H6zM4 10h16a2 2 0 0 1 2 2v6h-4v4H6v-4H2v-6a2 2 0 0 1 2-2zm4 7v3h8v-3z"/></svg>
        905-555-0147
      </li>
      <li>
        <svg viewBox="0 0 24 24" aria-label="Website"><path d="M12 2a10 10 0 1 0 0 20 10 10 0 0 0 0-20zm6.9 6h-3a15 15 0 0 0-1.3-3.9A8 8 0 0 1 18.9 8zM12 4c.8 1.2 1.5 2.5 1.9 4h-3.8c.4-1.5 1.1-2.8 1.9-4zM4.3 14a8 8 0 0 1 0-4h3.4a16 16 0 0 0 0 4zm.8 2h3a15 15 0 0 0 1.3 3.9A8 8 0 0 1 5.1 16zm3-8h-3a8 8 0 0 1 4.3-3.9A15 15 0 0 0 8.1 8zM12 20c-.8-1.2-1.5-2.5-1.9-4h3.8c-.4 1.5-1.1 2.8-1.9 4zm2.3-6H9.7a14 14 0 0 1 0-4h4.6a14 14 0 0 1 0 4zm.3 5.9A15 15 0 0 0 15.9 16h3a8 8 0 0 1-4.3 3.9zM16.3 14a16 16 0 0 0 0-4h3.4a8 8 0 0 1 0 4z"/></svg>
        www.rmdentalcare.example
      </li>
    </ul>
  </div>
</section>

</body>
</html>
```